MD Trailcraft & Wildland Expo

I need a 1 page flyer for promotion of an upcoming sportsman and outdoor show(expo). would like the flyer to be able to be printed in B&W and color! show will include all things to do with the out doors, hunting fishing boating hiking atv camping rvs motorcycles. the event will have a kids zone, events games and activities for kids. there will be vendors showing the newest products. guest speakers and industry experts giving training and advice. this show will have something for everyone. food trucks and concessions. 200+ vendors. waterfould calling competition. deer/buck scoring casting competition for kids 3D Archery competitions

Target Market(s)

anyone event open to all ages!

Colors
ec1f27
000000
fbed22

Requirements
Must have
• date- september 1-2 2018
• location Penwick county fair 4817 millbrook rd east caldon MD 21638
• facebook - mdtrailcraftexpo
• email mdtrailcraftexpo@mailvento.com
• web www.mdtrailcraftexpo-demo.com
• vendor spaces still available! sign up now space going fast
Nice to have
• would like some thing that can be both printed in B&W and Color, and still have a great affect.
Should not have
• open to any suggestions

```html
<!DOCTYPE html>
<html lang="en">
<head>
<meta charset="utf-8">
<title>MD Trailcraft Expo – Vendor Flyer</title>
<link href="https://fonts.googleapis.com/css2?family=Bebas+Neue&family=Montserrat:wght@400;500;700;800&family=Oswald:wght@300;400&family=Raleway:wght@400&display=swap" rel="stylesheet">
<style>
  :root{
    --red:#ec1f27;
    --black:#000000;
    --ink:#1a1a1a;
    --yellow:#fbed22;
    --white:#ffffff;
    --rule:#8a8a8a;
  }
  *{margin:0;padding:0;box-sizing:border-box}
  html,body{width:927px;height:1200px;overflow:hidden;background:var(--white)}
  .flyer{position:relative;width:850px;height:1100px;transform:scale(1.090588);transform-origin:0 0;overflow:hidden;background:var(--white);font-family:"Montserrat",sans-serif;color:var(--ink)}
  .photo{position:absolute}
  .photo--archery{left:0;top:0;width:280px;height:440px;background:radial-gradient(circle at 65% 45%,#c9b08a 0%,#8a6e4e 35%,#3b332c 80%)}
  .photo--jetski{left:287px;top:0;width:276px;height:420px;background:linear-gradient(180deg,#566f86 0%,#314a63 55%,#9fb3c5 100%)}
  .photo--atv{left:570px;top:0;width:280px;height:420px;background:linear-gradient(160deg,#e8dcae 0%,#c8a865 45%,#6b5a3e 100%)}
  .backdrop{position:absolute;left:0;top:0;width:850px;height:1030px;background:linear-gradient(180deg,#ffffff 0%,#f6f7f8 45%,#e6e9ec 70%,#c3c9d0 85%,#7d8794 100%);clip-path:polygon(0 425px,850px 338px,850px 1030px,0 1030px)}
  .masthead{position:absolute;left:0;top:0;width:850px;height:520px}
  .masthead__title{font-family:"Bebas Neue",sans-serif;font-size:100px;fill:var(--white)}
  .masthead__date{font-family:"Raleway",sans-serif;font-size:46px;fill:var(--ink)}
  .intro{position:absolute;left:0;top:494px;width:850px;text-align:center;font-weight:800;font-size:17.5px;line-height:25px;color:var(--ink)}
  .offer-list{position:absolute;top:558px;list-style:none;font-size:16.5px;font-weight:500;letter-spacing:0.2px}
  .offer-list li{height:27.2px;line-height:22px;position:relative;padding-left:14px;white-space:nowrap}
  .offer-list li::before{content:"";position:absolute;left:0;top:8px;width:6px;height:6px;border-radius:50%;background:var(--red)}
  .offer-list--one{left:73px}
  .offer-list--two{left:337px}
  .offer-list--three{left:590px}
  .pitch{position:absolute;left:22px;top:797px;width:806px;height:33px;border-radius:9px;background:var(--red);color:var(--white);font-weight:700;font-size:15.5px;line-height:33px;text-align:center}
  .expect{position:absolute;left:0;top:843px;width:850px;text-align:center;font-size:24px;font-weight:400;color:var(--ink)}
  .headline{position:absolute;left:0;top:870px;width:850px;text-align:center;font-size:40px;font-weight:800;color:var(--red)}
  .venue{position:absolute;left:12px;top:925px;width:826px;height:105px;border-radius:12px;background:var(--white);display:flex;flex-direction:column;align-items:center;justify-content:center;gap:6px;text-align:center}
  .venue__name{font-weight:800;font-size:24px;color:var(--ink)}
  .venue__address{font-weight:500;font-size:17px;color:var(--ink)}
  .footer{position:absolute;left:0;top:1030px;width:850px;height:70px;background:var(--black);color:var(--white)}
  .cta{position:absolute;left:28px;top:21px;font-weight:700;font-size:19px;color:var(--red)}
  .divider{position:absolute;top:16px;width:1px;height:38px;background:var(--rule)}
  .divider--a{left:248px}.divider--b{left:524px}
  .phone{position:absolute;left:262px;top:7px;width:250px;text-align:center;font-family:"Oswald",sans-serif;font-weight:300;font-size:31px;line-height:36px;letter-spacing:0.3px;white-space:nowrap}
  .web{position:absolute;left:262px;top:49px;width:250px;text-align:center;font-size:8.5px;letter-spacing:0.2px;white-space:nowrap}
  .social{position:absolute;left:538px;font-size:11.5px;letter-spacing:0;display:flex;align-items:center;gap:8px;white-space:nowrap}
  .social--mail{top:14px}.social--page{top:37px}
  .dot{width:18px;height:18px;border-radius:50%;background:var(--red);display:flex;align-items:center;justify-content:center;flex:none}
</style>
</head>
<body>
<div class="flyer">
  <div class="photo photo--archery" role="img" aria-label="Archer drawing a bow at a target"></div>
  <div class="photo photo--jetski" role="img" aria-label="Rider on a jet ski spraying water"></div>
  <div class="photo photo--atv" role="img" aria-label="ATV rider kicking up dirt"></div>
  <div class="backdrop" role="img" aria-label="Faint motocross rider jumping over a misty background"></div>

  <svg class="masthead" viewBox="0 0 850 520" aria-label="MD Trailcraft Expo, September 1-2, 2018">
    <polygon points="38,372 793,282 800,342 42,452" fill="var(--red)"/>
    <text class="masthead__title" x="72" y="432" textLength="688" lengthAdjust="spacingAndGlyphs" transform="rotate(-6.6 72 432)">MD TRAILCRAFT EXPO</text>
    <text class="masthead__date" x="155" y="482" textLength="510" lengthAdjust="spacingAndGlyphs" transform="rotate(-4.7 155 482)">SEPTEMBER 1-2,2018</text>
  </svg>

  <p class="intro">OVER 60,000 SQFT OF INDOOR AND 30,000+ SQFT OUTDOOR<br>PRODUCTS AND SERVICES INCLUDING:</p>

  <ul class="offer-list offer-list--one">
    <li>SPORTS EQUIPMENT</li><li>TACKLE &amp; BAIT</li><li>TAXIDERMISTS</li><li>CHARTER BOATS</li>
    <li>TRAILERS</li><li>OUTDOOR MEGAZINES</li><li>CAMPING&nbsp; EQUIPMENT</li><li>JET SKIS</li>
  </ul>
  <ul class="offer-list offer-list--two">
    <li>CAMPERS</li><li>MOTORCYCLES</li><li>OUTFITTERS</li><li>GOLF RESORTS</li>
    <li>SPORTING CLUBS</li><li>CAMP GROUNDS</li><li>HUNTING SUPPLIES</li><li>ARCHERY</li>
  </ul>
  <ul class="offer-list offer-list--three">
    <li>BOAT</li><li>ATV'S</li><li>GUNS</li><li>KNIVES</li>
    <li>RV'S</li><li>TRUCKS</li><li>GAME CALLS</li><li>AND MUCH MORE...</li>
  </ul>

  <p class="pitch">SELL YOUR PRODUCTS AND SERVICES TO THOUSANDS OF PEOPLE IN ONE WEEKEND!!</p>
  <p class="expect">WE ARE EXPECTING 2 DAY ATTENDANCE TO</p>
  <p class="headline">TOP 15,000 PEOPLE!</p>

  <div class="venue">
    <p class="venue__name">PENWICK COUNTY FAIR</p>
    <p class="venue__address">4817 MILLBROOK RD EAST CALDON MD 21638</p>
  </div>

  <footer class="footer">
    <span class="cta">CONTACT US TODAY</span>
    <span class="divider divider--a"></span>
    <span class="phone">DANA 410-555-0148</span>
    <span class="web">WWW.MDTRAILCRAFTEXPO-DEMO.COM</span>
    <span class="divider divider--b"></span>
    <span class="social social--mail">
      <span class="dot"><svg width="11" height="8" viewBox="0 0 11 8"><rect x="0.5" y="0.5" width="10" height="7" fill="none" stroke="#fff"/><polyline points="0.5,0.5 5.5,4.5 10.5,0.5" fill="none" stroke="#fff"/></svg></span>
      MDTRAILCRAFTEXPO@MAILVENTO.COM
    </span>
    <span class="social social--page">
      <span class="dot"></span>
      @MDTRAILCRAFTEXPO
    </span>
  </footer>
</div>
</body>
</html>
```